Info Graphic

We’re looking for a graphic designer to create an infographic that visually communicates Kestrel Verge Co’s three-phase approach to vegetation management, specifically for high-risk assets like airports. The infographic should effectively tell the story of how our process improves sustainability, reduces costs, and enhances efficiency compared to conventional vegetation management practices.

Project Scope:
Objective:

Develop an engaging and professional infographic that illustrates the three key phases of KVC’s approach:
Phase 1 - Audit – Identifying existing vegetation and reviewing current management practices.
Phase 2 Work out a Program – Developing a site-specific plan to address identified issues and meet project KPIs. Matrix of options and budgets
Phase 3 Implementation, Monitoring & Assessment – Full program delivery, stakeholder engagement, project management. Monitor and assess the progress of the program, adjusting strategies as needed, and providing a final report for ongoing management.

Key Requirements:
The infographic should be visually compelling and easy to understand.
It should highlight the benefits of our approach (cost savings, environmental sustainability, efficiency).

The design should align with Kestrel Verge Co’s branding (colors, typography, style). I can provide some of our other design work so as it remains inline with our current branding options.

I've included the phase detail, an example of something we'd like as well as an example of our PPT.

```html
<!DOCTYPE html>
<html lang="en">
<head>
<meta charset="utf-8">
<title>Kestrel Verge Co – Three-Phase Approach</title>
<link rel="stylesheet" href="https://fonts.googleapis.com/css2?family=Open+Sans:wght@300;400;600;700&display=swap">
<style>
  :root {
    --green: #76bc21;
    --ink: #1f1f1f;
    --header-grey: #e4e4e4;
    --card-border: #cfcfcf;
    --white: #ffffff;
  }
  * { margin: 0; padding: 0; box-sizing: border-box; }
  html, body { width: 1200px; height: 675px; overflow: hidden; background: var(--white); }
  body { position: relative; font-family: "Open Sans", Arial, sans-serif; color: var(--ink); }

  .headline { position: absolute; left: 131px; top: 57px; height: 72px; border-left: 7px solid var(--green); padding-left: 18px; }
  .headline p { font-size: 23px; line-height: 25px; color: var(--green); font-weight: 400; letter-spacing: 0.2px; white-space: nowrap; }
  .headline .headline-strong { font-weight: 700; }

  .phase-card { position: absolute; top: 185px; width: 277px; height: 356px; border: 1.5px solid var(--card-border); border-radius: 8px; background: var(--white); box-shadow: 0 10px 10px -8px rgba(0,0,0,0.18); }
  .phase-card.p1 { left: 157px; }
  .phase-card.p2 { left: 462px; }
  .phase-card.p3 { left: 767px; }

  .phase-head { position: absolute; left: 0; top: 0; width: 100%; height: 65px; background: var(--header-grey); border-radius: 7px 7px 0 0; }
  .phase-icon { position: absolute; left: 20px; top: 10px; width: 47px; height: 47px; border-radius: 50%; background: linear-gradient(135deg, #cfe8ad, #a8d46d); }
  .phase-title { position: absolute; left: 88px; top: 12px; font-size: 30px; font-weight: 300; color: var(--green); letter-spacing: -0.5px; line-height: 40px; white-space: nowrap; }

  .phase-list { position: absolute; left: 24px; top: 136px; list-style: none; }
  .phase-list li { position: relative; padding-left: 17px; font-size: 15.5px; line-height: 25.1px; white-space: nowrap; }
  .phase-list li::before { content: ""; position: absolute; left: 0; top: 10px; width: 5px; height: 5px; border-top: 2px solid var(--green); border-right: 2px solid var(--green); transform: rotate(45deg); }
  .phase-card.p2 .phase-list { left: 10px; }
  .phase-card.p2 .phase-list li { padding-left: 14px; }
  .phase-card.p3 .phase-list { left: 16px; }

  .band { position: absolute; left: 157px; top: 256px; width: 890px; height: 44px; }
  .band-label { position: absolute; top: 256px; height: 44px; line-height: 44px; color: var(--white); font-weight: 600; font-size: 14px; letter-spacing: 2.6px; text-align: center; white-space: nowrap; }
  .band-label.assess { left: 157px; width: 280px; }
  .band-label.solve { left: 452px; width: 296px; letter-spacing: 3.4px; }
  .band-label.guide { left: 772px; width: 274px; font-size: 13.5px; letter-spacing: 1.6px; }

  .brand { position: absolute; left: 1060px; top: 636px; width: 120px; text-align: center; font-size: 11px; font-weight: 400; color: #555; letter-spacing: 0.3px; white-space: nowrap; }
  .brand-mark { position: absolute; left: 1108px; top: 606px; width: 24px; height: 24px; border-radius: 50%; border: 2px solid var(--green); }

  .footer-bar { position: absolute; left: 0; bottom: 0; width: 1200px; height: 12px; background: var(--green); }
</style>
</head>
<body>
  <div class="headline">
    <p>FIND A PROBLEM</p>
    <p class="headline-strong">QUANTIFY THE PROBLEM</p>
    <p>SOLUTION</p>
  </div>

  <section class="phase-card p1">
    <div class="phase-head">
      <div class="phase-icon" role="img" aria-label="Audit icon: document with chart and magnifier"></div>
      <h2 class="phase-title">PHASE 1</h2>
    </div>
    <ul class="phase-list">
      <li>Site Audit</li>
      <li>Survey &amp; Mapping</li>
      <li>Agronomic Assessment</li>
      <li>Data Analysis</li>
      <li>Issue ID</li>
      <li>Report &amp; Recommendations</li>
      <li>Scorecard</li>
      <li>Risk Identification</li>
    </ul>
  </section>

  <section class="phase-card p2">
    <div class="phase-head">
      <div class="phase-icon" role="img" aria-label="Solve icon: light bulb made of puzzle pieces"></div>
      <h2 class="phase-title">PHASE 2</h2>
    </div>
    <ul class="phase-list">
      <li>Program Options Matrix</li>
      <li>Multiyear Budget Forecast</li>
      <li>Stakeholder Engagement</li>
      <li>ID Guide</li>
      <li>Program Implementation Strategy</li>
      <li>Handbook</li>
      <li>Manual Guide</li>
      <li>Risk Mitigation</li>
    </ul>
  </section>

  <section class="phase-card p3">
    <div class="phase-head">
      <div class="phase-icon" role="img" aria-label="Monitor icon: light bulb and gear within cycle arrows"></div>
      <h2 class="phase-title">PHASE 3</h2>
    </div>
    <ul class="phase-list">
      <li>Full Program</li>
      <li>Detailed Implementation Plan</li>
      <li>Training</li>
      <li>Stakeholder Management</li>
      <li>Project Management</li>
      <li>Delivery Support</li>
      <li>Scientific Monitoring</li>
      <li>Reporting</li>
    </ul>
  </section>

  <svg class="band" viewBox="0 0 890 44" aria-hidden="true">
    <polygon points="0,0 280,0 288,22 280,44 0,44" fill="#76bc21"/>
    <polyline points="284,0 293,22 284,44" fill="none" stroke="#76bc21" stroke-width="3"/>
    <polygon points="292,0 596,0 604,22 596,44 292,44 301,22" fill="#76bc21"/>
    <polyline points="600,0 609,22 600,44" fill="none" stroke="#76bc21" stroke-width="3"/>
    <polygon points="608,0 886,0 886,44 608,44 617,22" fill="#76bc21"/>
  </svg>
  <div class="band-label assess">ASSESS + UNDERSTAND</div>
  <div class="band-label solve">SOLVE</div>
  <div class="band-label guide">GUIDE - MONITOR - EVALUATE</div>

  <div class="brand-mark"></div>
  <div class="brand">Kestrel Verge Co</div>

  <div class="footer-bar"></div>
</body>
</html>
```